Wedding page for Linda and Daniel

we need a webpage for our wedding. The website contains the basic information of the wedding. like general information, timetable, map, contact information and a photo section, more you find in the attached word document.
attached you see our invitation cards, design should have similarties like the cards.
We like green colours and as its a weeding page it can be romantic. :-)
Industry/Entity Type
Wedding
Coding
Coded - Design and coding required
Number of Pages Required
3 page
Font styles to use
Serif
Sans Serif
Decorative
Script
Colors
a5ce39
Requirements
Must have
- a clear structure and a simple navigation as there are 5 to 7 navigation points
- The weeding date should be clearly visible 26.05.2018.
- All labels and translation have to be editable by my (in HTML code or psd code is fine) --> the final page will be in german
Nice to have
- if the webdesign has some similarities with the wedding card.
- if there is a time counter till the wedding is coming.
- a modern way to display the program of the wedding day.
- the domain is kolvarenplitz.ch and would be cool to integrate somehow.
- if the website should be responsive.
Should not have
- no special logo or something needed.

```html
<!DOCTYPE html>
<html lang="en">
<head>
<meta charset="utf-8">
<title>Linda &amp; Daniel – 26.05.2018</title>
<link rel="stylesheet" href="https://fonts.googleapis.com/css2?family=Playfair+Display:wght@400&family=Open+Sans:wght@400;600&display=swap">
<style>
:root{
  --green:#a5ce39;
  --green-dark:#93ba2c;
  --btn-top:#8fc23a;
  --btn-bottom:#5f9a1c;
  --ink:#3a3a3a;
  --muted:#8a8a8a;
  --label-red:#e0262b;
  --panel:#f7f7f7;
  --white:#ffffff;
  --frame:#e8e8e8;
}
*{margin:0;padding:0;box-sizing:border-box}
html,body{width:1200px;height:2177px;overflow:hidden;background:var(--white)}
body{position:relative;font-family:"Open Sans",Arial,sans-serif;color:var(--ink)}
.serif{font-family:"Playfair Display",Georgia,serif}
.abs{position:absolute}

/* hero */
.hero{position:absolute;left:0;top:0;width:1200px;height:534px;
  background:linear-gradient(100deg,#7fc4b0 0%,#b8dc9a 30%,#e6ef9e 60%,#f3f3a6 100%);}
.hero-couple{position:absolute;left:355px;top:105px;width:300px;height:429px;
  background:linear-gradient(180deg,rgba(90,90,70,.55) 0%,rgba(120,110,90,.45) 55%,rgba(235,230,215,.7) 100%);
  border-radius:120px 120px 20px 20px}
.hero-shore{position:absolute;left:0;top:450px;width:1200px;height:84px;
  background:linear-gradient(180deg,rgba(240,240,220,.2),rgba(225,220,190,.85))}
.hero-title{left:0;width:1200px;top:34px;text-align:center;color:var(--white);font-size:38px;letter-spacing:.5px}
.date-label{left:657px;top:238px;font-size:19px;color:#4a4a3a}
.date-value{left:654px;top:260px;font-size:52px;color:#3e3e34}
.btn-details{left:660px;top:355px;width:144px;height:50px;line-height:50px;text-align:center;
  color:var(--white);font-size:14px;border-radius:3px;
  background:linear-gradient(180deg,var(--btn-top),var(--btn-bottom))}

/* navigation */
.main-nav{position:absolute;left:0;top:534px;width:1200px;height:51px;background:var(--green)}
.nav-item{position:absolute;top:0;height:51px;line-height:51px;transform:translateX(-50%);
  color:var(--white);font-size:11.5px;white-space:nowrap}
.nav-item.active{background:var(--green-dark);width:58px;text-align:center}

/* welcome */
.section-title{left:0;width:1200px;text-align:center;font-size:29px;color:var(--ink)}
.portrait{width:170px;height:170px;border-radius:50%;border:4px solid #efefef;
  box-shadow:0 0 0 1px #e0e0e0}
.portrait.bride{background:radial-gradient(circle at 50% 60%,#e9c6b3,#8a5a45 85%)}
.portrait.groom{background:radial-gradient(circle at 50% 60%,#d9a98c,#6a4a38 85%)}
.person-name{width:420px;text-align:center;font-size:29px}
.person-text{width:440px;text-align:center;font-size:11.5px;line-height:23px;color:var(--muted)}

/* photos */
.photo-band{position:absolute;left:0;top:1122px;width:1200px;height:489px;background:var(--panel)}
.photo{top:1278px;width:293px;height:231px;border:5px solid var(--white);box-shadow:0 0 0 1px var(--frame)}
.photo.bouquet{left:132px;background:linear-gradient(135deg,#f5e8e4,#e8b9a6 55%,#c9a48e)}
.photo.aisle{left:453px;background:linear-gradient(180deg,#e8e6ea,#bdb7c1 50%,#f2f2f2)}
.photo.balloons{left:773px;background:linear-gradient(180deg,#d9b486,#b08a63 55%,#4d5a3a)}
.arrow{top:1408px}

/* time table */
.tt-heading{left:129px;top:1684px;font-size:29px}
.tt-label{left:132px;font-size:11.5px;color:var(--label-red);letter-spacing:.3px}
.tt-value{left:132px;font-size:19px}
.tt-text{left:132px;top:1926px;width:440px;font-size:11.5px;line-height:23px;color:var(--muted)}
.map-frame{left:599px;top:1692px;width:470px;height:274px;border:5px solid var(--white);
  box-shadow:0 0 0 1px var(--frame);background:linear-gradient(135deg,#e9e6dc,#dfe4cf 40%,#ece8d8 70%,#d8e3c8)}
.map-card{left:726px;top:1789px;width:197px;height:141px;background:var(--white);
  box-shadow:0 1px 4px rgba(0,0,0,.2);padding:12px 0 0 14px;font-size:11px;color:#555}
.map-row{display:flex;align-items:flex-start;gap:10px;height:28px}
.map-row svg{flex:none;margin-top:2px}

/* footer */
.site-footer{position:absolute;left:0;top:2052px;width:1200px;height:125px;background:var(--green)}
.social{top:2082px;width:32px;height:32px;border:1.5px solid var(--white);border-radius:50%}
.copyright{left:0;top:2132px;width:1200px;text-align:center;color:var(--white);font-size:10px}
</style>
</head>
<body>

<header class="hero">
  <div class="hero-couple" role="img" aria-label="Photo of the bride and groom embracing on a sunny shore"></div>
  <div class="hero-shore"></div>
</header>
<h1 class="abs serif hero-title">LINDA &amp; DANIEL</h1>
<div class="abs serif date-label">DATE</div>
<div class="abs serif date-value">26.05.2018</div>
<a class="abs serif btn-details">VIEW DEATAILS</a>

<nav class="main-nav">
  <span class="nav-item serif active" style="left:160px">HOME</span>
  <span class="nav-item serif" style="left:239px">THE STORY</span>
  <span class="nav-item serif" style="left:363px">GENERAL INFORMATION</span>
  <span class="nav-item serif" style="left:525px">INFORMATION EVENT</span>
  <span class="nav-item serif" style="left:673px">CONTACT TO FAMILY</span>
  <span class="nav-item serif" style="left:820px">ONLINE INVITATION</span>
  <span class="nav-item serif" style="left:942px">PICTURES</span>
  <span class="nav-item serif" style="left:1036px">CONTACT</span>
</nav>

<section class="welcome">
  <h2 class="abs serif section-title" style="top:630px">WELCOME TO LINDA &amp; DANIEL</h2>
  <div class="abs portrait bride" style="left:252px;top:725px" role="img" aria-label="Portrait of Linda"></div>
  <div class="abs portrait groom" style="left:764px;top:725px" role="img" aria-label="Portrait of Daniel"></div>
  <h3 class="abs serif person-name" style="left:122px;top:932px">LINDA</h3>
  <h3 class="abs serif person-name" style="left:646px;top:932px">DANIEL</h3>
  <p class="abs person-text" style="left:117px;top:990px">Lorem ipsum dolor sit amet, consectetur adipiscing elit, sed do eiusmod tempor incididunt ut labore et dolore magna aliqua.</p>
  <p class="abs person-text" style="left:636px;top:990px">Lorem ipsum dolor sit amet, consectetur adipiscing elit, sed do eiusmod tempor incididunt ut labore et dolore magna aliqua.</p>
</section>

<section class="photos">
  <div class="photo-band"></div>
  <h2 class="abs serif section-title" style="top:1173px">OUR PHOTO</h2>
  <div class="abs photo bouquet" role="img" aria-label="Bride holding a bouquet of peach roses"></div>
  <div class="abs photo aisle" role="img" aria-label="Couple walking down a church aisle"></div>
  <div class="abs photo balloons" role="img" aria-label="Couple kissing holding colourful balloons"></div>
  <svg class="abs arrow" style="left:88px" width="16" height="30" viewBox="0 0 16 30"><path d="M14 2 2 15l12 13" fill="none" stroke="#555" stroke-width="1.5"/></svg>
  <svg class="abs arrow" style="left:1086px" width="16" height="30" viewBox="0 0 16 30"><path d="M2 2l12 13L2 28" fill="none" stroke="#555" stroke-width="1.5"/></svg>
</section>

<section class="time-table">
  <h2 class="abs serif tt-heading">TIME TABLE</h2>
  <div class="abs serif tt-label" style="top:1741px">DATE :</div>
  <div class="abs serif tt-value" style="top:1765px">26.05.2018</div>
  <div class="abs serif tt-label" style="top:1817px">LOCATION:</div>
  <div class="abs serif tt-value" style="top:1843px">LOREM IPSUM DOLOR SIT AMET</div>
  <div class="abs serif tt-label" style="top:1893px">INFORMATION EVENT :</div>
  <p class="abs tt-text">Lorem ipsum dolor sit amet, consectetur adipiscing elit, sed do eiusmod tempor incididunt ut labore et dolore magna aliqua.</p>

  <div class="abs map-frame" role="img" aria-label="Street map of the wedding location"></div>
  <div class="abs map-card">
    <div class="map-row">
      <svg width="12" height="12" viewBox="0 0 12 12"><path d="M2 1h3l1 3-2 1a7 7 0 0 0 3 3l1-2 3 1v3a1 1 0 0 1-1 1A10 10 0 0 1 1 2a1 1 0 0 1 1-1z" fill="#444"/></svg>
      <span>408-555-0192</span></div>
    <div class="map-row">
      <svg width="12" height="12" viewBox="0 0 12 12"><rect x="3" y="1" width="6" height="3" fill="#444"/><rect x="1" y="4" width="10" height="5" rx="1" fill="#444"/><rect x="3" y="8" width="6" height="3" fill="#777"/></svg>
      <span>408-555-0147</span></div>
    <div class="map-row">
      <svg width="12" height="12" viewBox="0 0 12 12"><rect x="1" y="2.5" width="10" height="7" fill="none" stroke="#444"/><path d="M1 2.5l5 4 5-4" fill="none" stroke="#444"/></svg>
      <span style="text-decoration:underline">info@kolvarenplitz.ch</span></div>
    <div class="map-row" style="height:auto">
      <svg width="12" height="12" viewBox="0 0 12 12"><path d="M6 11S2 6.5 2 4.5a4 4 0 0 1 8 0C10 6.5 6 11 6 11z" fill="#444"/><circle cx="6" cy="4.5" r="1.4" fill="#fff"/></svg>
      <span>#2868 Lorem ipsum dolor sit amet, consectetur</span></div>
  </div>
</section>

<footer class="site-footer"></footer>
<span class="abs social" style="left:547px" aria-label="Social link"></span>
<span class="abs social" style="left:583px" aria-label="Social link"></span>
<span class="abs social" style="left:620px" aria-label="Social link"></span>
<p class="abs copyright">©2016 kolvarenplitz.ch . All Rights Reserved.</p>

</body>
</html>
```